Crane Ledger claims recovery services

Its a new company in Dubai UAE. The company activity is debt management, debt collection, loans settlements and restructuring. The company involved in any business or sector requires debt management including government entities, Medical & Health care sector, Banks & finance companies, SME's and commercial business.

Target Market(s)

government entities, Medical & Health care sector, Banks & finance companies, SME's and commercial business.

Industry/Entity Type

Financial Service

Number of Pages Required

5+ page

Requirements
Must have
• Focus on the services not the team and clients
Should not have
• Colorful . Shouldn't have Client testimonial and our clients

```html
<!DOCTYPE html>
<html lang="en">
<head>
<meta charset="utf-8">
<title>Crane Ledger — Claims Recovery Services</title>
<link rel="stylesheet" href="https://fonts.googleapis.com/css2?family=Roboto+Condensed:wght@400;700&family=Open+Sans:wght@400;700&family=Lato:wght@900&display=swap">
<style>
:root{
  --brand:#2b6690;
  --brand-dark:#285578;
  --grey:#a3a6aa;
  --ink:#555;
  --light:#efefef;
  --white:#fff;
}
*{margin:0;padding:0;box-sizing:border-box}
html,body{width:723px;height:1200px;overflow:hidden;background:var(--white)}
body{position:relative;font-family:"Open Sans",sans-serif;color:var(--ink)}
.abs{position:absolute}
.cond{font-family:"Roboto Condensed",sans-serif}

.hero{left:0;top:0;width:723px;height:396px;
  background:linear-gradient(180deg,rgba(255,255,255,0) 55%,rgba(150,140,125,.55) 100%),
  linear-gradient(110deg,#3d8fb8 0%,#a9cfe0 30%,#e8e8de 60%,#f6e6b8 100%)}
.hero-notch{left:0;top:395px}
.main-nav{left:0;top:14px;width:723px;display:flex;justify-content:center;gap:27px;font-size:13px;color:#2a3a4a}
.main-nav .active{color:var(--brand)}
.nav-rule{left:46px;top:48px;width:631px;height:1px;background:rgba(255,255,255,.7)}
.brand-mark{left:323px;top:92px;width:76px;height:76px;border-radius:50%;background:var(--brand)}
.brand-name{left:0;top:198px;width:723px;text-align:center;font-size:34px;color:var(--brand);letter-spacing:1px}
.hero-title{left:0;top:280px;width:723px;text-align:center;font-family:"Lato",sans-serif;font-weight:900;font-size:29px;color:var(--white);letter-spacing:-.5px}

.section-title{left:0;width:723px;text-align:center;font-size:28px;color:#8a8a8a}
.section-title b{font-weight:400;color:var(--brand)}
.intro{left:78px;top:486px;width:567px;text-align:center;font-size:9.6px;line-height:15.2px}

.service-img{top:556px;width:126px;height:85px}
.service-title{top:552px;font-size:16px;color:var(--brand)}
.service-text{top:576px;width:170px;font-size:9.6px;line-height:15px}
.read-more{top:626px;font-size:9.6px;font-weight:700;color:var(--brand)}

.call-band{left:46px;top:675px}
.call-label{left:60px;top:700px;font-size:19px;color:var(--white)}
.call-number{left:219px;top:696px;font-size:23px;font-weight:700;color:var(--white)}
.call-note{left:395px;top:688px;width:270px;font-size:9.6px;line-height:15px;color:var(--white)}
.call-mail{left:397px;top:724px;font-size:12.5px;color:var(--brand);display:flex;align-items:center;gap:6px}

.news{left:0;top:794px;width:723px;height:270px;background:var(--light)}
.news-img{top:866px;width:141px;height:85px}
.news-title{top:957px;font-size:9.6px;color:var(--brand)}
.news-date{top:971px;font-size:9px;color:#999;display:flex;gap:5px;align-items:center}
.news-text{top:987px;width:145px;font-size:9.6px;line-height:15px}

.footer{left:0;top:1064px;width:723px;height:136px;background:var(--brand-dark);color:var(--white)}
.foot-nav{left:47px;top:1081px;display:flex;gap:25px;font-size:11.5px;color:var(--white)}
.foot-rule{left:46px;top:1111px;width:631px;height:1px;background:rgba(255,255,255,.25)}
.foot-heading{left:47px;top:1122px;font-size:13px;color:var(--white)}
.foot-text{font-size:9px;line-height:15px;color:var(--white)}
</style>
</head>
<body>

<div class="abs hero" role="img" aria-label="Hazy city skyline with a tall broadcast tower beside a river at sunrise"></div>
<svg class="abs hero-notch" width="723" height="30" viewBox="0 0 723 30"><path d="M314 0 C336 0 344 25 361 25 C378 25 386 0 408 0 Z" fill="#8d8478"/></svg>

<nav class="abs main-nav cond">
  <span class="active">HOME</span><span>ABOUT</span><span>SERVICES</span><span>CLIENTS</span><span>BLOG</span><span>CONTACT</span>
</nav>
<div class="abs nav-rule"></div>
<div class="abs brand-mark"></div>
<div class="abs brand-name cond">CRANE LEDGER</div>
<h1 class="abs hero-title">MAKING DEBT WORK FOR YOU</h1>

<h2 class="abs section-title cond" style="top:444px">WELCOME TO <b>CRANE LEDGER</b></h2>
<p class="abs intro">We are a Claims Recovery and Debt Management Services company based in Dubai, United Arab Emirates. The Crane Ledger team handles a comprehensive range of debt recoveries, such as invoices; insurance payments; supplier and rent payments; and personal and business loans, for individuals and businesses across an array of industries.</p>

<div class="abs service-img" style="left:46px;background:linear-gradient(135deg,#e6eef5,#b9cfe0)" role="img" aria-label="Hands reviewing financial charts on a tablet"></div>
<h3 class="abs service-title cond" style="left:184px;font-weight:400">Recovery Solutions</h3>
<p class="abs service-text" style="left:184px">Our experience has taught us that when it comes to recovery, it always pays to find the most amicable...</p>
<span class="abs read-more" style="left:185px">READ MORE »</span>

<div class="abs service-img" style="left:376px;background:linear-gradient(135deg,#c8d4dc,#8b9aa6)" role="img" aria-label="Business team meeting around a table"></div>
<h3 class="abs service-title cond" style="left:513px;font-weight:400">Debt Management</h3>
<p class="abs service-text" style="left:513px">At Crane Ledger, we pull together our wisdom and expertise to make debt work for you...</p>
<span class="abs read-more" style="left:514px">READ MORE »</span>

<svg class="abs call-band" width="631" height="82" viewBox="0 0 631 82">
  <polygon points="0,0 332,0 308,82 0,82" fill="#2b6690"/>
  <polygon points="340,0 631,0 631,82 316,82" fill="#a3a6aa"/>
  <circle cx="146" cy="37" r="18" fill="none" stroke="#fff" stroke-width="1.5"/>
  <path d="M139 29 l4-1 2 5-2 2 c1 3 3 5 6 6 l2-2 5 2-1 4 c-9 0-16-7-16-16z" fill="#fff"/>
</svg>
<div class="abs call-label cond">CALL US NOW</div>
<div class="abs call-number cond">123 456 7890</div>
<p class="abs call-note">Lorem Ipsum is simply dummy text of the printing and typesetting industry.</p>
<div class="abs call-mail"><svg width="15" height="11" viewBox="0 0 15 11"><rect x=".75" y=".75" width="13.5" height="9.5" fill="none" stroke="#2b6690" stroke-width="1.5"/><path d="M1 1l6.5 5 6.5-5" fill="none" stroke="#2b6690" stroke-width="1.5"/></svg>info@craneledger.com</div>

<div class="abs news"></div>
<h2 class="abs section-title cond" style="top:826px">RECENT <b>NEWS</b></h2>

<div class="abs news-img" style="left:46px;background:linear-gradient(135deg,#e9eef0,#9aa7b0)" role="img" aria-label="Two colleagues in a business discussion"></div>
<div class="abs news-img" style="left:210px;background:linear-gradient(135deg,#eeeae4,#a08b6e)" role="img" aria-label="Advisor meeting a client at a desk"></div>
<div class="abs news-img" style="left:373px;background:linear-gradient(135deg,#dfe6ee,#5a6a7c)" role="img" aria-label="Business handshake"></div>
<div class="abs news-img" style="left:535px;background:linear-gradient(135deg,#3f6fb4,#bcd3ec)" role="img" aria-label="Glass office tower seen from below"></div>

<div class="abs news-title" style="left:48px">Lorem Ipsum is dummy text.</div>
<div class="abs news-date" style="left:47px">▦ 11 June 2016</div>
<p class="abs news-text" style="left:47px">Lorem Ipsum is simply dummy text of the printing and type setting industry.</p>
<div class="abs news-title" style="left:212px">Lorem Ipsum is dummy text.</div>
<div class="abs news-date" style="left:211px">▦ 10 June 2016</div>
<p class="abs news-text" style="left:211px">Lorem Ipsum is simply dummy text of the printing and type setting industry.</p>
<div class="abs news-title" style="left:375px">Lorem Ipsum is dummy text.</div>
<div class="abs news-date" style="left:374px">▦ 09 June 2016</div>
<p class="abs news-text" style="left:374px">Lorem Ipsum is simply dummy text of the printing and type setting industry.</p>
<div class="abs news-title" style="left:537px">Lorem Ipsum is dummy text.</div>
<div class="abs news-date" style="left:536px">▦ 08 June 2016</div>
<p class="abs news-text" style="left:536px">Lorem Ipsum is simply dummy text of the printing and type setting industry.</p>

<footer class="abs footer"></footer>
<nav class="abs foot-nav"><span>Home</span><span>About</span><span>Services</span><span>Client</span><span>Blog</span><span>Contact</span></nav>
<svg class="abs" style="left:555px;top:1071px" width="124" height="32" viewBox="0 0 124 32">
  <circle cx="17" cy="16" r="15.5" fill="#fff"/>
  <circle cx="61" cy="16" r="15" fill="none" stroke="#fff" stroke-width="1.2"/>
  <circle cx="105" cy="16" r="15" fill="none" stroke="#fff" stroke-width="1.2"/>
</svg>
<div class="abs foot-rule"></div>
<div class="abs foot-heading">Contact Us</div>

<svg class="abs" style="left:46px;top:1143px" width="400" height="32" viewBox="0 0 400 32">
  <g fill="none" stroke="#fff" stroke-width="1.2">
    <circle cx="16" cy="16" r="15"/><circle cx="179" cy="16" r="15"/><circle cx="342" cy="16" r="15"/>
  </g>
  <path d="M16 8a5 5 0 0 1 5 5c0 4-5 10-5 10s-5-6-5-10a5 5 0 0 1 5-5z" fill="#fff"/><circle cx="16" cy="13" r="1.8" fill="#285578"/>
  <path d="M173 9l3-1 2 4-2 2c1 2 2 4 5 5l2-2 4 2-1 3c-8 0-13-5-13-13z" fill="#fff"/>
  <rect x="335.5" y="11.5" width="13" height="9" fill="none" stroke="#fff" stroke-width="1.2"/><path d="M336 12l6 5 6-5" fill="none" stroke="#fff" stroke-width="1.2"/>
</svg>
<p class="abs foot-text" style="left:83px;top:1145px;width:110px">Lorem Ipsum is dummy text of the printing.</p>
<p class="abs foot-text" style="left:246px;top:1151px">123 456 7890</p>
<p class="abs foot-text" style="left:409px;top:1151px">info@craneledger.com</p>
<p class="abs foot-text" style="left:536px;top:1145px">© <b>CRANE LEDGER</b> - 2016.<br>All Righst Reserved.</p>

</body>
</html>
```